TLPB Business Card Design

Business card for sole operator professional civil and traffic engineer.
Clients are developers and planners who require assistance with traffic strategic master planning advice and design development for access and infrastructure associated with the development.
Colours already in use are greens for the business name and black for other legend. The attached file shows the letterhead template which is currently in use.
Target Market(s)
Professional Clients in development industry
Most clients known to the Principal and card is mostly required to allow ongoing contact
Industry/Entity Type
Business
Contact Information for Business Card
DESMOND HALVERTON CONSULTING SERVICES
ABN 37 818 502 194
PO Box 871 KERRAWAY NSW 2619
Desmond Halverton 0431 558 906
desmond.halverton@quillmarsh.net

```html
<!DOCTYPE html>
<html lang="en">
<head>
<meta charset="utf-8">
<title>TLPB Business Card Design</title>
<link rel="stylesheet" href="https://fonts.googleapis.com/css2?family=Montserrat:wght@600;700&family=Rajdhani:wght@500;600&display=swap">
<style>
  :root {
    --green: #8cc63f;
    --green-deep: #6dbb4f;
    --card-front: #141414;
    --card-back: #262626;
    --ink-light: #f2f2f2;
    --ink-muted: #bdbdbd;
    --page: #ffffff;
  }
  * { box-sizing: border-box; margin: 0; padding: 0; }
  html, body { width: 1200px; height: 1134px; overflow: hidden; background: var(--page); }
  .canvas { position: relative; width: 1200px; height: 1134px; }

  .card { position: absolute; width: 520px; height: 300px; overflow: hidden; }
  .card--front { background: var(--card-front); }
  .card--back { background: var(--card-back); display: flex; flex-direction: column; align-items: center; justify-content: center; }

  .corner { position: absolute; width: 80px; height: 80px; fill: var(--green); }
  .corner--tl { top: 0; left: 0; }
  .corner--br { bottom: 0; right: 0; }

  .brand-mark { font-family: "Montserrat", sans-serif; font-weight: 700; color: var(--green); line-height: 1; letter-spacing: 2px; }
  .brand-name { font-family: "Montserrat", sans-serif; font-weight: 700; color: var(--green); letter-spacing: 1px; line-height: 1.2; }
  .brand-tag { font-family: "Montserrat", sans-serif; font-weight: 600; color: var(--ink-muted); letter-spacing: 3px; line-height: 1.2; }

  .front-brand { position: absolute; left: 40px; top: 95px; width: 200px; }
  .front-brand .brand-mark { font-size: 62px; }
  .front-brand .brand-name { font-size: 10px; margin-top: 8px; }
  .front-brand .brand-tag { font-size: 7px; }

  .divider { position: absolute; left: 262px; top: 60px; width: 2px; height: 180px; background: var(--green); }

  .contact { position: absolute; left: 290px; top: 82px; font-family: "Rajdhani", sans-serif; color: var(--ink-light); }
  .contact__name { font-family: "Montserrat", sans-serif; font-weight: 700; font-size: 14px; color: var(--green); letter-spacing: 1px; margin-bottom: 10px; }
  .contact__row { display: flex; align-items: center; gap: 7px; font-size: 13px; font-weight: 500; margin-bottom: 5px; white-space: nowrap; }
  .contact__row svg { width: 11px; height: 11px; fill: var(--green); flex: none; }
  .contact__abn { font-size: 13px; font-weight: 500; margin-top: 12px; padding-left: 60px; }

  .back-brand { text-align: center; }
  .back-brand .brand-mark { font-size: 96px; }
  .back-brand .brand-name { font-size: 17px; margin-top: 10px; }
  .back-brand .brand-tag { font-size: 10px; letter-spacing: 6px; }

  .pos-front { left: 50px; top: 110px; }
  .pos-back { left: 630px; top: 110px; }
  .small { transform: scale(0.55); transform-origin: top left; }
  .pos-front-small { left: 600px; top: 860px; }
  .pos-back-small { left: 895px; top: 860px; }

  .lockup { position: absolute; left: 30px; top: 830px; }
  .lockup .brand-mark { font-size: 200px; }
  .lockup .brand-name { font-size: 38px; margin-top: 18px; letter-spacing: 2px; }
</style>
</head>
<body>
<main class="canvas">

  <section class="card card--front pos-front">
    <svg class="corner corner--tl" viewBox="0 0 80 80"><polygon points="0,0 80,0 0,80"/></svg>
    <svg class="corner corner--br" viewBox="0 0 80 80"><polygon points="80,0 80,80 0,80"/></svg>
    <div class="front-brand">
      <div class="brand-mark">TLPB</div>
      <div class="brand-name">DESMOND HALVERTON</div>
      <div class="brand-tag">CONSULTING SERVICES</div>
    </div>
    <div class="divider"></div>
    <div class="contact">
      <div class="contact__name">DESMOND HALVERTON</div>
      <div class="contact__row"><svg viewBox="0 0 10 10"><path d="M5 0a3.5 3.5 0 0 0-3.5 3.5C1.5 6 5 10 5 10s3.5-4 3.5-6.5A3.5 3.5 0 0 0 5 0zm0 5a1.4 1.4 0 1 1 0-2.8A1.4 1.4 0 0 1 5 5z"/></svg>PO Box 871 KERRAWAY NSW 2619</div>
      <div class="contact__row"><svg viewBox="0 0 10 10"><path d="M2 0l2 2.5-1 1.2a6 6 0 0 0 3.3 3.3l1.2-1L10 8l-1.5 2C4 10 0 6 0 1.5z"/></svg>0431 558 906</div>
      <div class="contact__row"><svg viewBox="0 0 10 10"><path d="M0 2h10v6H0zM0 2l5 3.5L10 2" stroke="#141414" stroke-width=".8"/></svg>desmond.halverton@quillmarsh.net</div>
      <div class="contact__abn">ABN 37 818 502 194</div>
    </div>
  </section>

  <section class="card card--back pos-back">
    <div class="back-brand">
      <div class="brand-mark">TLPB</div>
      <div class="brand-name">DESMOND HALVERTON</div>
      <div class="brand-tag">CONSULTING SERVICES</div>
    </div>
  </section>

  <div class="lockup">
    <div class="brand-mark">TLPB</div>
    <div class="brand-name">DESMOND HALVERTON</div>
  </div>

  <section class="card card--front pos-front-small small">
    <div class="front-brand">
      <div class="brand-mark">TLPB</div>
      <div class="brand-name">DESMOND HALVERTON</div>
      <div class="brand-tag">CONSULTING SERVICES</div>
    </div>
    <div class="divider"></div>
    <div class="contact">
      <div class="contact__name">DESMOND HALVERTON</div>
      <div class="contact__row"><svg viewBox="0 0 10 10"><path d="M5 0a3.5 3.5 0 0 0-3.5 3.5C1.5 6 5 10 5 10s3.5-4 3.5-6.5A3.5 3.5 0 0 0 5 0zm0 5a1.4 1.4 0 1 1 0-2.8A1.4 1.4 0 0 1 5 5z"/></svg>PO Box 871 KERRAWAY NSW 2619</div>
      <div class="contact__row"><svg viewBox="0 0 10 10"><path d="M2 0l2 2.5-1 1.2a6 6 0 0 0 3.3 3.3l1.2-1L10 8l-1.5 2C4 10 0 6 0 1.5z"/></svg>0431 558 906</div>
      <div class="contact__row"><svg viewBox="0 0 10 10"><path d="M0 2h10v6H0zM0 2l5 3.5L10 2" stroke="#141414" stroke-width=".8"/></svg>desmond.halverton@quillmarsh.net</div>
      <div class="contact__abn">ABN 37 818 502 194</div>
    </div>
  </section>

  <section class="card card--back pos-back-small small">
    <div class="back-brand">
      <div class="brand-mark">TLPB</div>
      <div class="brand-name">DESMOND HALVERTON</div>
      <div class="brand-tag">CONSULTING SERVICES</div>
    </div>
  </section>

</main>
</body>
</html>
```